limo company looking for a graphic business card with professional look and feel

Looking for a business card design that can give you the full picture of the limo company by looking at the card - we provide airport service, wedding, birthday, night out, etc... we have sedans, suvs , limos, and party buses. I want the business card to have a professional look because we are targetting corporate clients as well as regular retail.
Info about the business can be found at: http://qivroe.example/Tm3Kx7
Target Market(s)
corporate clients and retail
Industry/Entity Type
Business
Contact Information for Business Card
I would like the logo and the name of the company to be in raised print - not sure if design makes a difference for that or just print - I need it designed in 350dpi
Requirements
Must have
- pictures of vehicle types (sedans, suvs, limos, party bus). pictures of interior of the limos if possible. list service types (weddings, birthdays, proms, airport transportation) & service areas (houston, the woodlands, spring, tomball, cypress, kingwood).
Nice to have
- nice professional look to it.

```html
<!DOCTYPE html>
<html lang="en">
<head>
<meta charset="utf-8">
<title>Crestline Coach – Business Card</title>
<link href="https://fonts.googleapis.com/css2?family=Arimo:wght@400;700&display=swap" rel="stylesheet">
<style>
  :root {
    --page: #e9e6e1;
    --card-black: #050505;
    --band-grey: #3a3a3a;
    --text-white: #ffffff;
    --text-soft: #d9d9d9;
    --rule: #4a4a4a;
    --photo-sky: #b9c4cc;
    --photo-road: #7d7f82;
  }
  * { box-sizing: border-box; margin: 0; padding: 0; }
  html, body { width: 1200px; height: 780px; overflow: hidden; }
  body {
    background: var(--page);
    font-family: "Arimo", Arial, sans-serif;
    color: var(--text-white);
    position: relative;
  }
  .card {
    position: absolute;
    top: 238px;
    width: 530px;
    height: 303px;
    background: var(--card-black);
    box-shadow: 0 8px 24px rgba(0,0,0,.28);
    overflow: hidden;
  }
  .card--front { left: 50px; }
  .card--back { left: 620px; }

  /* Front */
  .front-top { position: absolute; left: 0; top: 0; width: 100%; height: 116px; }
  .brand { position: absolute; left: 26px; top: 40px; display: flex; align-items: center; gap: 8px; }
  .brand__mark { width: 10px; height: 10px; background: var(--text-white); }
  .brand__name { font-size: 20px; font-weight: 400; line-height: 1.1; }
  .contact-person { position: absolute; right: 22px; top: 22px; text-align: right; }
  .contact-person__name { font-size: 24px; font-weight: 400; }
  .contact-person__title { font-size: 14px; color: var(--text-soft); margin-top: 2px; }
  .contact-person__phone { font-size: 14px; margin-top: 10px; display: flex; justify-content: flex-end; align-items: center; gap: 8px; }
  .photo-strip { position: absolute; left: 0; top: 116px; width: 100%; height: 124px; display: flex; gap: 4px; background: var(--card-black); }
  .photo { flex: 1; }
  .photo--1 { background: linear-gradient(180deg, #8f9aa3 0%, #5b5f63 55%, #2a2b2d 100%); }
  .photo--2 { background: linear-gradient(180deg, #cfe0ea 0%, #6f8b62 45%, #1e2226 100%); }
  .photo--3 { background: linear-gradient(180deg, #d7e2ea 0%, #9aa2a8 50%, #121416 100%); }
  .photo--4 { background: linear-gradient(180deg, #c9d6dc 0%, #8c9294 55%, #c7c9ca 100%); }
  .front-band { position: absolute; left: 0; bottom: 0; width: 100%; height: 63px; background: var(--band-grey); display: flex; justify-content: space-between; align-items: center; padding: 0 22px; font-size: 15px; }
  .contact-line { display: flex; align-items: center; gap: 9px; }
  .icon { width: 16px; height: 16px; flex: none; }

  /* Back */
  .back-vehicle { position: absolute; left: 40px; top: 40px; width: 460px; height: 220px; background: radial-gradient(ellipse at center, #1c1c1c 0%, rgba(5,5,5,0) 70%); }
  .back-brand { position: absolute; right: 26px; top: 28px; display: flex; align-items: center; gap: 8px; }
  .services { position: absolute; left: 30px; top: 96px; }
  .service-group { margin-bottom: 12px; }
  .service-group__title { font-size: 16px; font-weight: 700; letter-spacing: .3px; padding-bottom: 3px; border-bottom: 1px solid var(--rule); width: 320px; margin-bottom: 4px; }
  .service-group__list { font-size: 14px; color: var(--text-soft); }
</style>
</head>
<body>
  <section class="card card--front" aria-label="Business card front">
    <div class="front-top">
      <div class="brand">
        <span class="brand__mark"></span>
        <span class="brand__name">Crestline Coach<br>&amp; Transportation</span>
      </div>
      <div class="contact-person">
        <div class="contact-person__name">Employee Name</div>
        <div class="contact-person__title">Managing Director</div>
        <div class="contact-person__phone">
          <span>123 456 7890</span>
          <svg class="icon" viewBox="0 0 16 16"><rect x="1" y="1" width="14" height="14" fill="#fff"/><rect x="5" y="3" width="6" height="10" rx="1" fill="#050505"/><rect x="6" y="4" width="4" height="5" fill="#fff"/></svg>
        </div>
      </div>
    </div>
    <div class="photo-strip">
      <div class="photo photo--1" role="img" aria-label="Photo of a black SUV"></div>
      <div class="photo photo--2" role="img" aria-label="Photo of a dark sedan beside palm trees"></div>
      <div class="photo photo--3" role="img" aria-label="Photo of a black stretch limousine"></div>
      <div class="photo photo--4" role="img" aria-label="Photo of a silver sedan on a coastal road"></div>
    </div>
    <div class="front-band">
      <div class="contact-line">
        <svg class="icon" viewBox="0 0 16 16"><rect x="1" y="1" width="14" height="14" fill="#fff"/><path d="M3 5h10v7H3z M3 5l5 4 5-4" fill="none" stroke="#3a3a3a" stroke-width="1.2"/></svg>
        <span>you@yourmail.example</span>
      </div>
      <div class="contact-line">
        <svg class="icon" viewBox="0 0 16 16"><rect x="1" y="1" width="14" height="14" fill="#fff"/><circle cx="8" cy="8" r="4.5" fill="none" stroke="#3a3a3a" stroke-width="1.1"/><path d="M3.5 8h9M8 3.5v9" stroke="#3a3a3a" stroke-width="1"/></svg>
        <span>www.yourweb.example</span>
      </div>
    </div>
  </section>

  <section class="card card--back" aria-label="Business card back">
    <div class="back-vehicle" role="img" aria-label="Faint photo of a stretch limousine"></div>
    <div class="back-brand">
      <span class="brand__mark"></span>
      <span class="brand__name">Crestline Coach<br>&amp; Transportation</span>
    </div>
    <div class="services">
      <div class="service-group">
        <div class="service-group__title">SERVICE</div>
        <div class="service-group__list">weddings | birthdays | proms | airport transportation</div>
      </div>
      <div class="service-group">
        <div class="service-group__title">SERVICE AREAS</div>
        <div class="service-group__list">houston | the woodlands | spring | tomball | cypress | kingwood</div>
      </div>
      <div class="service-group">
        <div class="service-group__title">VEHICLE TYPES</div>
        <div class="service-group__list">sedans | suvs | limos | party bus</div>
      </div>
    </div>
  </section>
</body>
</html>
```